Custom unique Stationary design for Logistics company

We need a custom, unique , elegant and luxurious full stationary design using our new logo, following these guidelines:
1- Business card: double sided, both sides uses the navy blue as the background main color (same as the code of the navy blue used in our logo).
2- envelope and folder: also use the same navy blue as the main background color.
3- book cover( notepad cover) : same thing with the navy blue
4- letterhead: feel free to use the combination of the colors in our logo.
5- rest of the items are up to your creativity

Target Market(s)

corporates and other businesses

Industry/Entity Type

Logistics and heavy machines contractors

Requirements
Must have
• Letterhead, business card, envelope, notepad cover, paper, file
Nice to have
• navy blue to be main background color for business card, envelope, notepad cover

```html
<!DOCTYPE html>
<html lang="en">
<head>
<meta charset="utf-8">
<title>Meridian Freight Letterhead</title>
<link href="https://fonts.googleapis.com/css2?family=Lato:wght@400;700;900&family=Montserrat:wght@400;500&family=Italianno&display=swap" rel="stylesheet">
<style>
  :root {
    --navy: #0f4a72;
    --orange: #ee6a35;
    --ink: #333333;
    --backdrop: #dedede;
    --paper: #ffffff;
  }
  * { margin: 0; padding: 0; box-sizing: border-box; }
  html, body { width: 1162px; height: 1200px; overflow: hidden; background: var(--backdrop); }
  .letterhead {
    position: absolute; left: 188px; top: 92px; width: 786px; height: 1018px;
    background: var(--paper); color: var(--ink);
    font-family: 'Lato', sans-serif;
    box-shadow: 0 2px 6px rgba(0,0,0,0.18);
    overflow: hidden;
  }
  .brand {
    position: absolute; left: 47px; top: 66px;
    display: flex; align-items: center; gap: 12px;
    font-family: 'Lato', sans-serif; font-weight: 900; font-size: 34px;
    color: var(--navy); letter-spacing: 0.5px;
  }
  .brand-dot { width: 22px; height: 22px; border-radius: 50%; background: var(--orange); }
  .contact {
    position: absolute; left: 565px; top: 44px;
    font-family: 'Montserrat', sans-serif; color: #222; white-space: nowrap;
  }
  .contact-address { font-size: 13px; line-height: 17px; margin-bottom: 6px; }
  .contact-line { display: flex; align-items: center; gap: 5px; font-size: 12px; line-height: 16px; }
  .contact-line svg { width: 8px; height: 8px; fill: var(--navy); }
  .header-rule { position: absolute; left: 47px; top: 172px; width: 694px; height: 3px; background: var(--navy); }
  .letter { position: absolute; left: 59px; top: 258px; width: 680px; font-size: 14px; }
  .date { margin-bottom: 17px; }
  .block { line-height: 17px; margin-bottom: 17px; }
  .salutation { font-weight: 700; font-size: 17px; margin: 12px 0 16px; }
  .letter p.body { font-size: 13.6px; letter-spacing: 0.2px; line-height: 16px; text-align: justify; margin-bottom: 16px; }
  .closing { margin-top: 36px; font-size: 13.5px; }
  .signature { font-family: 'Italianno', cursive; font-size: 42px; color: #222; margin-top: 8px; }
  .footer-accent { position: absolute; left: 0; bottom: 40px; width: 786px; height: 3px; background: var(--orange); }
  .footer-band { position: absolute; left: 0; bottom: 0; width: 786px; height: 32px; background: var(--navy); }
</style>
</head>
<body>
  <div class="letterhead">
    <div class="brand"><span class="brand-dot"></span>Meridian Freight</div>

    <div class="contact">
      <div class="contact-address">Northgate Star 2100 Park<br>Harbor Ave WD Suite 310</div>
      <div class="contact-line"><svg viewBox="0 0 10 10"><path d="M2 0h2l1 3-1.5 1a6 6 0 0 0 2.5 2.5L7 5l3 1v2a2 2 0 0 1-2 2A8 8 0 0 1 0 2a2 2 0 0 1 2-2z"/></svg>011 555 0142</div>
      <div class="contact-line"><svg viewBox="0 0 10 10"><rect x="0" y="2" width="10" height="6"/></svg>info@meridianfreight.com</div>
      <div class="contact-line"><svg viewBox="0 0 10 10"><circle cx="5" cy="5" r="5"/></svg>www.meridianfreight.com</div>
    </div>

    <div class="header-rule"></div>

    <div class="letter">
      <div class="date">January-03-2020</div>
      <div class="block">Mr, Peter Lane<br>President</div>
      <div class="block">Crestview Holdings<br>48 Orchard Road, Suite# 12<br>City, State, 120023</div>
      <div class="salutation">Dear Mr, Peter</div>
      <p class="body">Lorem ipsum dolor sit amet, consectetur adipisicing elit, sed do eiusmod tempor incididunt ut labore et dolore magna aliqua. Ut enim ad minim veniam, quis nostrud exercitation ullamco laboris nisi ut aliquip ex ea commodo consequat. Duis aute irure dolor in reprehenderit in voluptate velit esse cillum dolore eu fugiat nulla pariatur.</p>
      <p class="body">Lorem ipsum dolor sit amet, consectetur adipisicing elit, sed do eiusmod tempor incididunt ut labore et dolore magna aliqua. Ut enim ad minim veniam, quis nostrud exercitation ullamco laboris nisi ut aliquip ex ea commodo consequat. Duis aute irure dolor in reprehenderit in voluptate velit esse cillum dolore eu fugiat nulla pariatur.</p>
      <p class="body">Lorem ipsum dolor sit amet, consectetur adipisicing elit, sed do eiusmod tempor incididunt ut labore et dolore magna aliqua. Ut enim ad minim veniam, quis nostrud exercitation ullamco laboris nisi ut aliquip ex ea commodo consequat.</p>
      <p class="body">Excepteur sint occaecat cupidatat non proident, sunt in culpa qui officia deserunt mollit anim id est laborum. re et dolore magnam aliquam quaerat voluptatem.</p>
      <div class="closing">Regards</div>
      <div class="signature">Daniel Reyes</div>
    </div>

    <div class="footer-accent"></div>
    <div class="footer-band"></div>
  </div>
</body>
</html>
```